sign business needs card design

I need a very clean design for my business card.
It is a sign company. Banners By Noon is the name of the business.
Our colors are orange, yellow. But I want a very professional card.
But you can use any colors. I like a black background with orange letters or a white back with a clean look. No cartoon or kiddy looking print. The info. I need on the card is as follows.
Banners By Noon
318.514.7702 ph.
318.514.7739 fax.
email.bannersbynoon@velmora.net
web.bannersbynooninc.example
4172 N. Calloway Ridge Ste. 2b
Dale Kessner

```html
<!DOCTYPE html>
<html lang="en">
<head>
<meta charset="utf-8">
<title>Banners By Noon – Business Card</title>
<link rel="stylesheet" href="https://fonts.googleapis.com/css2?family=Poiret+One&family=Questrial&display=swap">
<style>
  :root {
    --page: #ffffff;
    --trim-guide: #b7dcec;
    --card-bg: #201a16;
    --accent: #e67a26;
    --accent-light: #f4c197;
    --ink-dark: #231e1a;
  }
  * { margin: 0; padding: 0; box-sizing: border-box; }
  html, body {
    width: 1200px;
    height: 741px;
    overflow: hidden;
    background: var(--page);
  }
  .canvas {
    position: relative;
    width: 1200px;
    height: 741px;
  }
  .guide {
    position: absolute;
    left: 0;
    width: 1200px;
    height: 2px;
    background: var(--trim-guide);
  }
  .guide--top { top: 7px; }
  .guide--bottom { top: 737px; }

  .card {
    position: absolute;
    left: 37px;
    top: 48px;
    width: 1132px;
    height: 651px;
    background: var(--card-bg);
    color: var(--accent);
    font-family: "Poiret One", "Century Gothic", sans-serif;
  }

  .contact-lines {
    position: absolute;
    left: 755px;
    top: 24px;
    width: 363px;
    font-size: 36px;
    line-height: 56px;
  }
  .contact-lines .row {
    display: flex;
    justify-content: space-between;
    white-space: nowrap;
  }

  .name-band {
    position: absolute;
    left: 0;
    top: 226px;
    width: 658px;
    height: 196px;
    background: linear-gradient(90deg, var(--accent-light) 0%, #eea06a 22%, var(--accent) 45%, var(--accent) 100%);
    color: var(--ink-dark);
    text-align: center;
  }
  .business-name {
    position: absolute;
    left: 0;
    width: 100%;
    top: 25px;
    font-family: "Poiret One", "Century Gothic", sans-serif;
    font-size: 66px;
    font-weight: 400;
    font-variant: small-caps;
    line-height: 1;
    letter-spacing: 1px;
    white-space: nowrap;
  }
  .person-name {
    position: absolute;
    left: 0;
    width: 100%;
    top: 106px;
    font-family: "Questrial", "Century Gothic", sans-serif;
    font-size: 43px;
    font-weight: 400;
    line-height: 1;
    white-space: nowrap;
  }

  .address-block {
    position: absolute;
    left: 40px;
    top: 458px;
    white-space: nowrap;
  }
  .address-block .street {
    font-size: 36px;
    line-height: 48px;
    letter-spacing: 0.5px;
  }
  .address-block .online {
    font-size: 33px;
    line-height: 44px;
    margin-top: 4px;
  }
</style>
</head>
<body>
  <main class="canvas">
    <div class="guide guide--top"></div>

    <section class="card" aria-label="Banners By Noon business card">
      <div class="contact-lines">
        <p class="row"><span>Phone:</span><span>318.514.7702</span></p>
        <p class="row"><span>Fax:</span><span>318.514.7739</span></p>
      </div>

      <div class="name-band">
        <h1 class="business-name">Banners By Noon</h1>
        <p class="person-name">Dale Kessner</p>
      </div>

      <address class="address-block" style="font-style: normal;">
        <p class="street">4172 N. Calloway Ridge Ste. 2b</p>
        <p class="online">bannersbynoon@velmora.net<br>www.bannersbynooninc.example</p>
      </address>
    </section>

    <div class="guide guide--bottom"></div>
  </main>
</body>
</html>
```